TFCS Truck Wrap Design

New Truck wrap design for our brand.

Varden Hollowmark Limited 2022 Black
Edgy, Eye catching, Decorative Concrete Coating com

Info on Truck
Logo
(800) 555-0147
CopperOtterShopSlabs.example
Free In-Garage Consultation
Give your Neighbors "Garage Envy"!

I attached a billboard to show some of our marketing
Fonts are
RR Beaver
Sansation
Rugen
Rubik

Target Market(s)

Upscale Homeowners

Industry/Entity Type

Concrete Coating

Font styles to use
Other font styles liked:
• RR Beaver, Sansation, Rugen, Rubik

Colors
EB3D1F
EC4F4E
F09395
F8D3D4
FCEDEE

```html
<!DOCTYPE html>
<html lang="en">
<head>
<meta charset="utf-8">
<title>TFCS Truck Wrap – Side Panel</title>
<link rel="stylesheet" href="https://fonts.googleapis.com/css2?family=Rubik:ital,wght@0,500;0,700;1,700;1,800&display=swap">
<style>
  :root {
    --wrap-black: #221f20;
    --wrap-charcoal: #2e2a2b;
    --brand-red: #eb3d1f;
    --brand-red-soft: #ec4f4e;
    --brand-red-deep: #a3231a;
    --text-white: #ffffff;
    --text-outline: #1a1718;
    --page: #ffffff;
  }
  * { margin: 0; padding: 0; box-sizing: border-box; }
  html, body { width: 1200px; height: 1200px; overflow: hidden; background: var(--page); }
  .canvas { position: relative; width: 1200px; height: 1200px; }

  .wrap-panel {
    position: absolute; left: 50px; top: 440px;
    width: 1100px; height: 320px;
    border-radius: 18px; overflow: hidden;
    background: var(--wrap-black);
  }
  .wrap-art { position: absolute; inset: 0; width: 100%; height: 100%; }

  .brand-block { position: absolute; left: 80px; top: 95px; }
  .brand-name {
    display: flex; align-items: center; gap: 18px;
    font-family: "Rubik", sans-serif; font-weight: 700;
    font-size: 44px; line-height: 1.05; letter-spacing: 1px;
    color: var(--text-white); text-transform: uppercase;
  }
  .brand-dot {
    width: 22px; height: 22px; border-radius: 50%;
    background: var(--brand-red); flex: none;
  }
  .brand-web {
    margin-top: 22px;
    font-family: "Rubik", sans-serif; font-style: italic; font-weight: 700;
    font-size: 19px; letter-spacing: 0.5px; color: var(--text-white);
  }

  .brand-mark-spot {
    position: absolute; left: 560px; top: 60px;
    width: 190px; height: 190px; border-radius: 50%;
    border: 10px solid var(--brand-red);
  }

  .offer-block {
    position: absolute; right: 60px; top: 44px; text-align: left;
    transform: rotate(-2deg);
  }
  .offer-phone {
    font-family: "Rubik", sans-serif; font-style: italic; font-weight: 800;
    font-size: 46px; color: var(--text-white);
    -webkit-text-stroke: 2px var(--text-outline); paint-order: stroke fill;
  }
  .offer-line {
    margin-top: 6px;
    font-family: "Rubik", sans-serif; font-style: italic; font-weight: 700;
    font-size: 24px; color: var(--text-white);
    -webkit-text-stroke: 1.5px var(--text-outline); paint-order: stroke fill;
  }
</style>
</head>
<body>
<main class="canvas">
  <section class="wrap-panel" aria-label="Truck wrap side panel">
    <svg class="wrap-art" viewBox="0 0 1100 320" preserveAspectRatio="none" aria-hidden="true">
      <defs>
        <linearGradient id="redSweep" x1="0" y1="0" x2="1" y2="0">
          <stop offset="0" stop-color="#eb3d1f" stop-opacity="0"/>
          <stop offset="0.35" stop-color="#c92a1e"/>
          <stop offset="1" stop-color="#ec4f4e"/>
        </linearGradient>
      </defs>
      <rect class="wrap-base" width="1100" height="320" fill="#221f20"/>
      <polygon class="sweep-low" points="430,320 1100,150 1100,320" fill="url(#redSweep)"/>
      <polygon class="sweep-high" points="720,0 1100,0 1100,250 860,320 780,320" fill="#eb3d1f"/>
      <polygon class="stripe" points="820,0 900,0 760,320 700,320" fill="#a3231a" opacity="0.55"/>
      <polygon class="stripe" points="960,0 1010,0 900,320 850,320" fill="#ec4f4e" opacity="0.6"/>
      <polygon class="stripe" points="1050,0 1100,0 1100,60 1020,200" fill="#a3231a" opacity="0.5"/>
      <polygon class="shadow-cut" points="1100,230 1100,320 980,320" fill="#221f20"/>
    </svg>

    <div class="brand-mark-spot" aria-hidden="true"></div>

    <div class="brand-block">
      <div class="brand-name"><span class="brand-dot"></span><span>Copper Otter<br>Shop Slabs</span></div>
      <div class="brand-web">CopperOtterShopSlabs.example</div>
    </div>

    <div class="offer-block">
      <div class="offer-phone">(800) 555-0147</div>
      <div class="offer-line">Free In Garage Consultation</div>
    </div>
  </section>
</main>
</body>
</html>
```